TaviLo Gastronomic Social Network

Tavi Lo is a Gastronomic Social Network that is focused on the relationship between restaurants and customers, creating new channels to communicate with themselves and developing new tools to modernize the classic menus. In Tavi Lo people will see images, videos and texts related on gastronomy shared by the bests restaurants of their cities in real time. Therefore the users will feel how easy is to choose a new restaurant only few minutes before leaving their homes and how useful is to choose a meal with the images of the digital menu in order to have the best experience possible.

Target Market(s)

The direct customers of the company are the restaurants, who pay monthly to post marketing content and their digital menu. The profile of the clients will not be too restrictive: from a restaurant that offers live music and drinks to a classic and expensive restaurant.

The final users of the product are families, couples, professionals and everyone who is interested in discovering new restaurants and good gastronomy.

Requirements
Must have
• We have the idea that after the splash screen show the last registered plates from the restaurants like in snapreel story. On the story we will show the plate for the current time like lunch or dinner, a logo of the restaurant, a small description and the price.
• When selected the plate the user will be redirected to a page will restaurant details showing the selected plate as first item on restaurant menu.
• For each plate we will have a page description showing ingredients, price, harmonization and button to reserve a table.
• Reserve a table is a page for reservation.
• Also we have a page for customer info, last selected plates and restaurants.

```html
<!DOCTYPE html>
<html lang="en">
<head>
<meta charset="utf-8">
<title>Tavi Lo – App Screens</title>
<link rel="stylesheet" href="https://fonts.googleapis.com/css2?family=Lato:wght@400;700;900&family=Playfair+Display:wght@400;700&display=swap">
<style>
:root{
  --orange:#E09A26;
  --orange-soft:#EDA83A;
  --plum:#5A2440;
  --plum-deep:#4A1C35;
  --ink:#2A2A2A;
  --grey:#9A9A9A;
  --line:#DADADA;
  --pill-grey:#BDBDBD;
  --white:#FFFFFF;
  --alert:#E0323A;
}
*{box-sizing:border-box;margin:0;padding:0}
html,body{width:1200px;height:720px;overflow:hidden;background:var(--white)}
body{font-family:'Lato',sans-serif;color:var(--ink)}
.canvas{position:relative;width:1200px;height:720px;overflow:hidden}
.stage{position:absolute;left:0;top:0;width:1500px;height:900px;transform:scale(.8);transform-origin:0 0}
.backdrop{position:absolute;inset:0}
.screen{position:absolute;overflow:hidden;background:var(--white)}
.abs{position:absolute}
.status{position:absolute;left:0;right:0;top:0;height:40px;font-size:10px;font-weight:700}
.status .time{position:absolute;left:22px;top:14px}
.status svg{position:absolute;right:18px;top:14px}
.light{color:var(--white)}
.serif{font-family:'Playfair Display',serif}
.photo{position:absolute}
.avatar{position:absolute;border-radius:50%;background:radial-gradient(circle at 50% 40%,#C9A48A,#6B4A3A);border:2px solid var(--white)}

/* splash */
.splash{left:24px;top:50px;width:274px;height:595px;background:var(--orange)}
.splash-mark{position:absolute;left:0;right:0;top:262px;text-align:center}
.splash-mark .dot{display:block;width:36px;height:36px;margin:0 auto 10px;border-radius:50%;background:var(--plum)}
.splash-mark .name{font-size:20px;color:var(--plum);font-weight:400}

/* story */
.story{left:306px;top:193px;width:275px;height:596px}
.story .photo{inset:0;background:linear-gradient(160deg,#6B6A4A 0%,#3A2E25 35%,#5A3B2C 60%,#2E2620 100%)}
.story .shade{position:absolute;inset:0;background:linear-gradient(180deg,rgba(0,0,0,.35),rgba(0,0,0,.1) 50%,rgba(0,0,0,.25))}
.resto-chip{position:absolute;left:20px;top:82px;display:flex;align-items:center;gap:10px;color:var(--white);font-size:11px;font-weight:700}
.resto-chip .disc{width:30px;height:30px;border-radius:50%;background:var(--white)}
.story .price{position:absolute;right:24px;top:76px;color:var(--white);font-size:28px}
.price sup{font-size:13px;vertical-align:top;position:relative;top:4px}
.story h1{position:absolute;left:19px;top:124px;color:var(--white);font-size:32px;font-weight:700}
.story p{position:absolute;left:20px;top:173px;width:220px;color:var(--white);font-size:11.5px;line-height:14px}
.btn-ghost{position:absolute;left:19px;top:249px;width:116px;height:40px;border:2px solid var(--white);border-radius:20px;color:var(--white);font-size:11px;display:flex;align-items:center;justify-content:center;gap:8px}
.progress{position:absolute;left:19px;top:543px;width:231px;height:3px;background:rgba(255,255,255,.85);border-radius:2px}

/* feed */
.feed{left:587px;top:153px;width:275px;height:595px}
.feed-head{position:absolute;left:0;right:0;top:40px;height:72px;box-shadow:0 3px 8px rgba(0,0,0,.06)}
.menu-icon{position:absolute;width:16px}
.menu-icon i{display:block;height:2px;background:#9A9A9A;margin-bottom:4px}
.wordmark{position:absolute;left:0;right:0;top:27px;text-align:center;font-size:16px;font-weight:900;color:var(--plum)}
.post-head{position:absolute;left:20px;display:flex;align-items:center;gap:10px}
.post-head .disc{width:28px;height:28px;border-radius:50%}
.post-head b{display:block;font-size:11px;font-weight:400;color:var(--ink)}
.post-head small{display:block;font-size:7px;color:var(--grey);margin-top:2px}
.live-bar{position:absolute;left:22px;top:287px;width:230px;height:38px;background:var(--orange);border-radius:0 0 3px 3px;color:var(--white);font-size:11px;display:flex;align-items:center;justify-content:space-between;padding:0 16px 0 18px}
.tabbar{position:absolute;left:0;right:0;bottom:0;height:93px;background:var(--plum)}
.tab{position:absolute;top:18px;width:60px;text-align:center;font-size:7px;color:#D9C6D0;font-weight:700}
.tab svg{display:block;margin:0 auto 6px}
.tab.active{color:var(--orange)}
.tab .badge{position:absolute;left:34px;top:-2px;width:6px;height:6px;border-radius:50%;background:var(--alert)}
.home-ind{position:absolute;left:88px;bottom:12px;width:100px;height:4px;border-radius:2px;background:#2A0F1F}

/* detail */
.detail{left:871px;top:19px;width:275px;height:871px}
.detail .hero{left:0;top:0;width:275px;height:253px;background:linear-gradient(135deg,#3C4A2A 0%,#6E5A3A 35%,#4A2A22 60%,#2E2622 100%)}
.btn-pill{position:absolute;border-radius:20px;font-size:8px;font-weight:900;letter-spacing:2px;color:var(--white);display:flex;align-items:center;justify-content:center}
.detail h2{position:absolute;left:0;right:0;top:295px;text-align:center;font-size:28px;font-weight:700}
.detail .price{position:absolute;left:0;right:0;top:327px;text-align:center;font-size:24px}
.detail .desc{position:absolute;left:30px;right:26px;top:371px;text-align:center;font-size:9.5px;line-height:12.5px;color:#A5A5A5;font-style:italic}
.brand-block{position:absolute;left:0;right:0;top:462px;text-align:center}
.brand-block .disc{display:block;width:38px;height:38px;margin:0 auto 14px;border-radius:50%;background:var(--alert)}
.brand-block b{display:block;font-size:11px;font-weight:400;color:#444}
.brand-block small{display:block;font-size:9.5px;color:#777;margin-top:4px}
.dish{position:absolute;top:566px}
.dish .thumb{height:127px;border-radius:2px}
.dish h4{font-family:'Playfair Display',serif;font-size:11px;font-weight:400;margin-top:10px;white-space:nowrap}
.dish p{font-size:9px;color:#AAA;line-height:12px;margin-top:4px;white-space:nowrap}
.detail .tabbar{height:92px}

/* reservation & profile */
.panel{box-shadow:0 2px 14px rgba(0,0,0,.08)}
.reserve{left:1154px;top:15px;width:276px;height:597px;background:#FCFCFC}
.panel-head{position:absolute;left:0;right:0;top:40px;height:72px;background:var(--white);box-shadow:0 3px 8px rgba(0,0,0,.06)}
.panel-title{position:absolute;left:0;right:0;text-align:center;font-size:11px;font-weight:900;letter-spacing:3.5px}
.back{position:absolute}
.label{position:absolute;font-size:11px;font-weight:700}
.muted{color:var(--grey);font-weight:400}
.rule{position:absolute;left:20px;width:231px;height:1px;background:var(--line)}
.day{position:absolute;top:342px;width:30px;text-align:center}
.day small{display:block;font-size:6px;color:#888;font-weight:700}
.day b{display:block;font-size:19px;font-weight:400;margin-top:1px}
.day.active{background:var(--orange);color:var(--white);height:37px;top:340px;padding-top:3px}
.day.active small{color:var(--white)}
.slot{position:absolute;top:394px;height:30px;border-radius:15px;font-size:9.5px;color:var(--white);display:flex;align-items:center;justify-content:center}
.profile{left:1154px;top:623px;width:278px;height:290px}
.person{position:absolute;left:126px;top:148px}
.person b{display:block;font-size:14px;font-weight:700}
.person small{display:block;font-size:11px;color:var(--grey);margin-top:4px}
.ptab{position:absolute;top:239px;font-size:10px}
</style>
</head>
<body>
<div class="canvas">
<div class="stage">

  <svg class="backdrop" width="1500" height="900" viewBox="0 0 1500 900" aria-hidden="true">
    <circle cx="437" cy="-40" r="290" fill="var(--orange)"/>
    <circle cx="640" cy="830" r="290" fill="var(--orange)"/>
    <circle cx="935" cy="195" r="135" fill="var(--orange)"/>
    <circle cx="160" cy="802" r="91" fill="var(--orange)"/>
    <circle cx="1500" cy="612" r="92" fill="var(--orange)"/>
  </svg>

  <!-- Splash -->
  <section class="screen splash">
    <div class="status light"><span class="time">9:41</span>
      <svg width="50" height="8" viewBox="0 0 50 8"><rect x="0" y="5" width="2" height="3" fill="#fff"/><rect x="3" y="3" width="2" height="5" fill="#fff"/><rect x="6" y="1" width="2" height="7" fill="#fff"/><rect x="9" y="0" width="2" height="8" fill="#fff"/><path d="M16 3a7 7 0 0 1 10 0l-1.5 1.5a5 5 0 0 0-7 0zM19 6a3 3 0 0 1 4 0l-2 2z" fill="#fff"/><rect x="32" y="1" width="14" height="6" rx="1.5" fill="#fff"/></svg>
    </div>
    <div class="splash-mark"><span class="dot"></span><span class="name serif">Tavi Lo</span></div>
  </section>

  <!-- Story -->
  <section class="screen story">
    <div class="photo" role="img" aria-label="Close-up photo of sliced grilled lamb steak with peppercorn sauce and vegetables"></div>
    <div class="shade"></div>
    <div class="status light"><span class="time">9:41</span>
      <svg width="50" height="8" viewBox="0 0 50 8"><rect x="0" y="5" width="2" height="3" fill="#fff"/><rect x="3" y="3" width="2" height="5" fill="#fff"/><rect x="6" y="1" width="2" height="7" fill="#fff"/><rect x="9" y="0" width="2" height="8" fill="#fff"/><path d="M16 3a7 7 0 0 1 10 0l-1.5 1.5a5 5 0 0 0-7 0zM19 6a3 3 0 0 1 4 0l-2 2z" fill="#fff"/><rect x="32" y="1" width="14" height="6" rx="1.5" fill="#fff"/></svg>
    </div>
    <div class="resto-chip"><span class="disc"></span>Nico Grill House</div>
    <div class="price serif"><sup>$</sup>99</div>
    <h1 class="serif">Lamb Steak</h1>
    <p>Lorem ipsum dolor sit amet, consectetur adipisicing elit, sed do eiusmod tempor incididunt ut labore et dolore magna aliqua. Ut enim ad minim veniam.</p>
    <div class="btn-ghost">I want this
      <svg width="14" height="8" viewBox="0 0 14 8"><path d="M0 4h12M9 1l3 3-3 3" stroke="#fff" stroke-width="1.2" fill="none"/></svg>
    </div>
    <div class="progress"></div>
  </section>

  <!-- Feed -->
  <section class="screen feed">
    <div class="status"><span class="time">9:41</span>
      <svg width="50" height="8" viewBox="0 0 50 8"><rect x="0" y="5" width="2" height="3" fill="#222"/><rect x="3" y="3" width="2" height="5" fill="#222"/><rect x="6" y="1" width="2" height="7" fill="#222"/><rect x="9" y="0" width="2" height="8" fill="#222"/><path d="M16 3a7 7 0 0 1 10 0l-1.5 1.5a5 5 0 0 0-7 0zM19 6a3 3 0 0 1 4 0l-2 2z" fill="#222"/><rect x="32" y="1" width="14" height="6" rx="1.5" fill="#222"/></svg>
    </div>
    <div class="feed-head">
      <div class="menu-icon" style="left:21px;top:31px"><i></i><i></i><i style="width:11px"></i></div>
      <div class="wordmark">Tavi Lo</div>
      <div class="avatar" role="img" aria-label="User profile photo" style="left:224px;top:20px;width:28px;height:28px"></div>
    </div>
    <div class="post-head" style="top:136px"><span class="disc" style="background:var(--alert)"></span><span><b>Nico Grill House</b><small>TODAY, 10:49</small></span></div>
    <div class="photo" role="img" aria-label="Photo of grilled lamb steak with roasted vegetables and sauce" style="left:22px;top:170px;width:230px;height:117px;border-radius:3px 3px 0 0;background:linear-gradient(120deg,#2E3A22,#6A5230 45%,#5A2E24 75%,#2A2420)"></div>
    <div class="live-bar"><span>All you can eat!</span><span>Watch Live&nbsp;&nbsp;›</span></div>
    <div class="post-head" style="top:349px"><span class="disc" style="background:#1E1A1A"></span><span><b>Vexa Bar</b><small>TODAY, 10:49</small></span></div>
    <div class="photo" role="img" aria-label="Photo of a table with drinks and shared plates" style="left:22px;top:384px;width:230px;height:120px;border-radius:3px;background:linear-gradient(120deg,#6A4A22,#B0783A 45%,#7A3A22 75%,#4A6A2A)"></div>
    <nav class="tabbar">
      <div class="tab" style="left:11px"><svg width="18" height="18" viewBox="0 0 18 18"><path d="M2 8l7-6 7 6v8H11v-5H7v5H2z" fill="none" stroke="#D9C6D0" stroke-width="1.2"/></svg>HOME</div>
      <div class="tab active" style="left:75px"><span class="badge"></span><svg width="18" height="18" viewBox="0 0 18 18"><path d="M9 17s-6-6-6-10a6 6 0 0 1 12 0c0 4-6 10-6 10z" fill="none" stroke="#E09A26" stroke-width="1.2"/><circle cx="9" cy="7" r="2" fill="none" stroke="#E09A26" stroke-width="1.2"/></svg>PLACES</div>
      <div class="tab" style="left:139px"><svg width="18" height="20" viewBox="0 0 18 20"><path d="M4 14V8a5 5 0 0 1 10 0v6l2 2H2zM7 18h4" fill="none" stroke="#D9C6D0" stroke-width="1.2"/></svg>MAPS</div>
      <div class="tab" style="left:203px"><svg width="20" height="20" viewBox="0 0 20 20"><circle cx="10" cy="10" r="8" fill="none" stroke="#D9C6D0" stroke-width="1.2"/><path d="M10 6v1M10 9v6" stroke="#D9C6D0" stroke-width="1.4"/></svg>HOW TO</div>
      <div class="home-ind"></div>
    </nav>
  </section>

  <!-- Dish detail -->
  <section class="screen detail">
    <div class="photo hero" role="img" aria-label="Overhead photo of lamb steak with vegetables and a bowl of sauce"></div>
    <div class="status light"><span class="time">9:41</span>
      <svg width="50" height="8" viewBox="0 0 50 8"><rect x="0" y="5" width="2" height="3" fill="#fff"/><rect x="3" y="3" width="2" height="5" fill="#fff"/><rect x="6" y="1" width="2" height="7" fill="#fff"/><rect x="9" y="0" width="2" height="8" fill="#fff"/><path d="M16 3a7 7 0 0 1 10 0l-1.5 1.5a5 5 0 0 0-7 0zM19 6a3 3 0 0 1 4 0l-2 2z" fill="#fff"/><rect x="32" y="1" width="14" height="6" rx="1.5" fill="#fff"/></svg>
    </div>
    <div class="menu-icon" style="left:21px;top:71px;width:14px"><i style="background:#fff"></i><i style="background:#fff"></i></div>
    <div class="avatar" role="img" aria-label="User profile photo" style="left:225px;top:62px;width:27px;height:27px"></div>
    <div class="btn-pill" style="left:60px;top:235px;width:159px;height:37px;background:var(--orange)">RESERVE TABLE</div>
    <h2 class="serif">Lamb Steak</h2>
    <div class="price serif"><sup>$</sup>99</div>
    <p class="desc">Gumbo beet greens corn soko endive gumbo gourd. Parsley shallot courgette tatsoi pea sprouts fava bean collard greens dandelion okra wakame tomato. Dandelion cucumber earthnut pea peanut soko zucchini.</p>
    <div class="brand-block"><span class="disc"></span><b>Nico Grill House</b><small>52 Maple Row Ave.</small></div>
    <div class="dish" style="left:-8px;width:100px"><div class="thumb" role="img" aria-label="Photo of grilled meat and vegetable skewers" style="background:linear-gradient(130deg,#6A5A2A,#C8A040 50%,#5A3A22)"></div><h4>&nbsp;&nbsp;Skwers</h4><p>&nbsp;&nbsp;bo beet greens corn<br>&nbsp;&nbsp;endive gumbo</p></div>
    <div class="dish" style="left:104px;width:113px"><div class="thumb" role="img" aria-label="Photo of a large cheeseburger" style="background:linear-gradient(130deg,#B07A3A,#6A3A22 50%,#C88A3A)"></div><h4>Burger Supreme</h4><p>Gumbo beet greens corn<br>soko endive gumbo</p></div>
    <div class="dish" style="left:229px;width:60px"><div class="thumb" role="img" aria-label="Photo of tacos" style="background:linear-gradient(130deg,#8A2A22,#D09A40 60%,#6A4A2A)"></div><h4>Taco's &amp;</h4><p>Gumbo bee<br>soko endiv</p></div>
    <nav class="tabbar">
      <div class="tab" style="left:11px"><svg width="18" height="18" viewBox="0 0 18 18"><path d="M2 8l7-6 7 6v8H11v-5H7v5H2z" fill="none" stroke="#D9C6D0" stroke-width="1.2"/></svg>HOME</div>
      <div class="tab active" style="left:75px"><span class="badge"></span><svg width="18" height="18" viewBox="0 0 18 18"><path d="M9 17s-6-6-6-10a6 6 0 0 1 12 0c0 4-6 10-6 10z" fill="none" stroke="#E09A26" stroke-width="1.2"/><circle cx="9" cy="7" r="2" fill="none" stroke="#E09A26" stroke-width="1.2"/></svg>PLACES</div>
      <div class="tab" style="left:139px"><svg width="18" height="20" viewBox="0 0 18 20"><path d="M4 14V8a5 5 0 0 1 10 0v6l2 2H2zM7 18h4" fill="none" stroke="#D9C6D0" stroke-width="1.2"/></svg>MAPS</div>
      <div class="tab" style="left:203px"><svg width="20" height="20" viewBox="0 0 20 20"><circle cx="10" cy="10" r="8" fill="none" stroke="#D9C6D0" stroke-width="1.2"/><path d="M10 6v1M10 9v6" stroke="#D9C6D0" stroke-width="1.4"/></svg>HOW TO</div>
      <div class="home-ind"></div>
    </nav>
  </section>

  <!-- Reservation -->
  <section class="screen panel reserve">
    <div class="status"><span class="time">9:41</span>
      <svg width="50" height="8" viewBox="0 0 50 8"><rect x="0" y="5" width="2" height="3" fill="#222"/><rect x="3" y="3" width="2" height="5" fill="#222"/><rect x="6" y="1" width="2" height="7" fill="#222"/><rect x="9" y="0" width="2" height="8" fill="#222"/><path d="M16 3a7 7 0 0 1 10 0l-1.5 1.5a5 5 0 0 0-7 0zM19 6a3 3 0 0 1 4 0l-2 2z" fill="#222"/><rect x="32" y="1" width="14" height="6" rx="1.5" fill="#222"/></svg>
    </div>
    <div class="panel-head">
      <svg class="back" style="left:23px;top:31px" width="18" height="12" viewBox="0 0 18 12"><path d="M17 6H2M7 1L2 6l5 5" stroke="#222" stroke-width="1.4" fill="none"/></svg>
      <div class="panel-title" style="top:30px">RESERVATION</div>
      <div class="avatar" role="img" aria-label="User profile photo" style="left:225px;top:21px;width:28px;height:28px"></div>
    </div>
    <div class="label" style="left:22px;top:156px">My Order</div>
    <div class="photo" role="img" aria-label="Small photo of the lamb steak dish" style="left:21px;top:190px;width:44px;height:41px;border-radius:2px;background:linear-gradient(130deg,#4A5A2A,#7A4A2A 60%,#3A2A22)"></div>
    <div class="abs serif muted" style="left:80px;top:190px;font-size:14px"><sup style="font-size:8px">$</sup>99</div>
    <div class="abs serif" style="left:81px;top:214px;font-size:13px">Lamb Steak</div>
    <div class="label" style="left:20px;top:262px">Table for</div>
    <div class="abs" style="right:25px;top:259px;font-size:14px">2 <span class="muted" style="font-size:11px">&nbsp;Persons</span></div>
    <div class="rule" style="top:282px"></div>
    <div class="label" style="left:20px;top:307px">Date</div>
    <div class="abs" style="right:25px;top:304px;font-size:14px">4 <span class="muted" style="font-size:11px">&nbsp;November</span></div>
    <div class="rule" style="top:327px"></div>
    <div class="day" style="left:12px"><small>TUE</small><b>1</b></div>
    <div class="day" style="left:49px"><small>WED</small><b>2</b></div>
    <div class="day" style="left:87px"><small>THU</small><b>3</b></div>
    <div class="day active" style="left:126px;width:28px"><small>FRI</small><b>4</b></div>
    <div class="day" style="left:162px"><small>SAT</small><b>5</b></div>
    <div class="day" style="left:199px"><small>SUN</small><b>6</b></div>
    <div class="day" style="left:236px;color:#BBB"><small>MO</small><b>7</b></div>
    <div class="slot" style="left:19px;width:83px;background:var(--orange)">1pm - 2pm</div>
    <div class="slot" style="left:108px;width:83px;background:var(--pill-grey)">3pm - 4pm</div>
    <div class="slot" style="left:198px;width:83px;background:var(--pill-grey)">5pm - 6pm</div>
    <div class="btn-pill" style="left:58px;top:484px;width:160px;height:40px;background:var(--plum)">RESERVE</div>
  </section>

  <!-- Profile -->
  <section class="screen panel profile">
    <div class="status"><span class="time">9:41</span>
      <svg width="50" height="8" viewBox="0 0 50 8"><rect x="0" y="5" width="2" height="3" fill="#222"/><rect x="3" y="3" width="2" height="5" fill="#222"/><rect x="6" y="1" width="2" height="7" fill="#222"/><rect x="9" y="0" width="2" height="8" fill="#222"/><path d="M16 3a7 7 0 0 1 10 0l-1.5 1.5a5 5 0 0 0-7 0zM19 6a3 3 0 0 1 4 0l-2 2z" fill="#222"/><rect x="32" y="1" width="14" height="6" rx="1.5" fill="#222"/></svg>
    </div>
    <svg class="back" style="left:23px;top:71px" width="18" height="12" viewBox="0 0 18 12"><path d="M17 6H2M7 1L2 6l5 5" stroke="#222" stroke-width="1.4" fill="none"/></svg>
    <div class="panel-title" style="top:71px">PROFILE</div>
    <div class="avatar" role="img" aria-label="Profile photo of the user" style="left:27px;top:122px;width:79px;height:79px;border:none"></div>
    <div class="person"><b>Marla Quinn</b><small>Dunmore, Ohio</small></div>
    <div class="ptab" style="left:59px;color:var(--orange)">Last Visited</div>
    <div class="abs" style="left:41px;top:258px;width:88px;height:2px;background:var(--orange)"></div>
    <div class="ptab muted" style="left:173px">My Info</div>
  </section>

</div>
</div>
</body>
</html>
```